Wine Label: Corvinte

The project is to create 3 wine labels. The brand name is "Corvinte"

What we need is to have 3 versions: red wine, white wine and rose.

The wine is for young and modern people, between 21 and 31 years old, so it need to be casual, modern and fun, but at the same time it needs to keep the Premiums of a good European wine.

It is from Italy.

Target Market(s)

Young adults, between 21 and 31 years old. wine lovers

Requirements
Must have
• - Modern colors (Black, silver, red, etc.)
• - Clean label
• - Clear font
• - Style
• - The brand + the type of wine (red, white or rose)
Nice to have
• - A symbol to represent the brand
Should not have
• - Many elements
• - No clear fonts
• - No funny colors

```html
<!DOCTYPE html>
<html lang="en">
<head>
<meta charset="utf-8">
<title>Corvinte Wine Labels</title>
<link rel="stylesheet" href="https://fonts.googleapis.com/css2?family=Poiret+One&display=swap">
<style>
  :root {
    --paper: #ffffff;
    --label-black: #000000;
    --rule-white: #ffffff;
    --white-wine: #f7f08e;
    --red-wine: #b01f24;
    --rose-wine: #ee8fbd;
    --type-white: #ffffff;
  }
  html, body {
    margin: 0;
    padding: 0;
    overflow: hidden;
    background: var(--paper);
  }
  .sheet {
    position: relative;
    width: 761px;
    height: 1200px;
    overflow: hidden;
    background: var(--paper);
  }
  .label {
    position: absolute;
    left: 0;
    width: 761px;
    height: 326px;
    background: var(--label-black);
    overflow: hidden;
  }
  .label--white { top: 0; --accent: var(--white-wine); }
  .label--red   { top: 428px; --accent: var(--red-wine); }
  .label--rose  { top: 874px; --accent: var(--rose-wine); }

  .accent-bar {
    position: absolute;
    left: 56px;
    top: 0;
    width: 22px;
    height: 100%;
    background: var(--accent);
    z-index: 2;
  }
  .side-rule {
    position: absolute;
    left: 90px;
    top: 0;
    width: 4px;
    height: 100%;
    background: var(--rule-white);
    z-index: 2;
  }
  .base-band {
    position: absolute;
    left: 0;
    top: 282px;
    width: 100%;
    height: 15px;
    background: var(--rule-white);
  }
  .base-rule {
    position: absolute;
    left: 0;
    top: 303px;
    width: 100%;
    height: 4px;
    background: var(--rule-white);
  }
  .brand-name {
    position: absolute;
    left: 98px;
    top: 0;
    width: 660px;
    height: 118px;
  }
  .brand-name text {
    font-family: "Poiret One", sans-serif;
    font-size: 150px;
    fill: var(--accent);
  }
  .wine-type {
    position: absolute;
    right: 189px;
    top: 250px;
    margin: 0;
    font-family: "Poiret One", sans-serif;
    font-size: 29px;
    line-height: 1;
    letter-spacing: -1px;
    color: var(--type-white);
    text-transform: uppercase;
  }
</style>
</head>
<body>
<main class="sheet">

  <section class="label label--white">
    <div class="accent-bar"></div>
    <div class="side-rule"></div>
    <svg class="brand-name" viewBox="0 0 660 118" aria-label="Corvinte">
      <text x="0" y="112" textLength="656" lengthAdjust="spacingAndGlyphs">CORVINTE</text>
    </svg>
    <p class="wine-type">White Wine</p>
    <div class="base-band"></div>
    <div class="base-rule"></div>
  </section>

  <section class="label label--red">
    <div class="accent-bar"></div>
    <div class="side-rule"></div>
    <svg class="brand-name" viewBox="0 0 660 118" aria-label="Corvinte">
      <text x="0" y="112" textLength="656" lengthAdjust="spacingAndGlyphs">CORVINTE</text>
    </svg>
    <p class="wine-type">Red Wine</p>
    <div class="base-band"></div>
    <div class="base-rule"></div>
  </section>

  <section class="label label--rose">
    <div class="accent-bar"></div>
    <div class="side-rule"></div>
    <svg class="brand-name" viewBox="0 0 660 118" aria-label="Corvinte">
      <text x="0" y="112" textLength="656" lengthAdjust="spacingAndGlyphs">CORVINTE</text>
    </svg>
    <p class="wine-type">Rose</p>
    <div class="base-band"></div>
    <div class="base-rule"></div>
  </section>

</main>
</body>
</html>
```